I am looking for a designer for my Gratitude Journal cover design. This is a daily gratitude journal designed for women. The interior features colored pages with a daily gratitude section, weekly habit tracker, and monthly reflection. The journal has enough space for a 12-week journaling.
Book size: 6x 9 inches
Paperback Print Book
Page count: 117
Platform: Nimbo BPX
Book title: I’m Unfinished, Who Cares?
Design Style:
-Boho style color and graphics, color choice is free but must follow color psychology, no pure black. The color and styling should correlate to the interior pages (In the attachment).
-There could be a female silhouette on the front cover, but not as big as the whole cover. (doesn’t have to if not looking good)
-No text or interior page preview on the back cover. Only pen name logo on the bottom middle of the back cover and make it small and subtle. (Pen name logo attached)
-Book title on front cover and spine, author name only on spine (Author name: Tobias Wexley).
-No other text on the front cover.
All design elements including fonts must be commercially licensed, and you must provide source files and commercial licenses of them together as part of the delivery.
nimbo.example

```html
<!DOCTYPE html>
<html lang="en">
<head>
<meta charset="utf-8">
<title>I’m Unfinished, Who Cares? — Cover Wrap</title>
<link href="https://fonts.googleapis.com/css2?family=Emilys+Candy&family=Montserrat:wght@400;500&display=swap" rel="stylesheet">
<style>
  :root {
    --paper: #ffffff;
    --cream: #f7f4ec;
    --sand: #f0e2c4;
    --tan: #e2b57d;
    --terracotta: #cd8a58;
    --rust: #a8683a;
    --teal-deep: #668f8d;
    --teal-soft: #8bb0b1;
    --teal-mist: #c5d9da;
    --ink: #414141;
    --guide: #9a9a9a;
  }
  * { margin: 0; padding: 0; box-sizing: border-box; }
  html, body {
    width: 1200px; height: 1000px; overflow: hidden;
    background: var(--paper);
  }
  .canvas { position: relative; width: 1200px; height: 1000px; }
  .cover-art { position: absolute; inset: 0; width: 1200px; height: 1000px; }

  .front-title {
    position: absolute;
    left: 690px; top: 318px; width: 382px;
    font-family: "Emilys Candy", cursive;
    font-weight: 400;
    font-size: 56px;
    line-height: 72px;
    color: var(--ink);
    text-align: center;
    letter-spacing: 1px;
  }
  .front-title span { display: block; white-space: nowrap; }

  .spine-title, .spine-author {
    position: absolute;
    writing-mode: vertical-rl;
    white-space: nowrap;
  }
  .spine-title {
    left: 592px; top: 132px;
    font-family: "Emilys Candy", cursive;
    font-size: 10px;
    color: var(--ink);
  }
  .spine-author {
    left: 593px; top: 574px;
    font-family: "Montserrat", sans-serif;
    font-size: 9.5px;
    font-weight: 500;
    letter-spacing: 0.6px;
    color: var(--cream);
  }

  .pen-name {
    position: absolute;
    left: 296px; top: 846px;
    display: flex; align-items: center; gap: 5px;
    font-family: "Montserrat", sans-serif;
    font-size: 8px;
    font-weight: 500;
    letter-spacing: 0.4px;
    color: var(--ink);
    white-space: nowrap;
  }
  .pen-name-dot {
    width: 22px; height: 22px; border-radius: 50%;
    background: var(--teal-deep);
  }
</style>
</head>
<body>
<main class="canvas">
  <svg class="cover-art" viewBox="0 0 1200 1000" xmlns="http://www.w3.org/2000/svg">
    <defs>
      <clipPath id="trim"><rect x="50" y="94" width="1099" height="811"/></clipPath>
      <radialGradient id="glow-teal">
        <stop offset="0" stop-color="var(--teal-soft)" stop-opacity="0.55"/>
        <stop offset="1" stop-color="var(--teal-soft)" stop-opacity="0"/>
      </radialGradient>
      <radialGradient id="glow-tan">
        <stop offset="0" stop-color="var(--tan)" stop-opacity="0.5"/>
        <stop offset="1" stop-color="var(--tan)" stop-opacity="0"/>
      </radialGradient>
      <radialGradient id="glow-rust">
        <stop offset="0" stop-color="var(--terracotta)" stop-opacity="0.3"/>
        <stop offset="1" stop-color="var(--terracotta)" stop-opacity="0"/>
      </radialGradient>
    </defs>

    <g clip-path="url(#trim)">
      <rect class="cover-base" x="50" y="94" width="1099" height="811" fill="var(--cream)"/>

      <!-- back cover shapes -->
      <path class="blob-sand" fill="var(--sand)" d="M50 94 H278 C292 150 292 200 272 215 C238 240 150 250 138 320 C130 360 150 420 140 437 H50 Z"/>
      <path class="blob-sand" fill="var(--sand)" d="M50 650 C120 640 200 680 270 720 C340 760 380 800 372 850 C365 890 330 905 300 905 H50 Z"/>
      <circle class="ring-terracotta" cx="137" cy="671" r="59" fill="var(--terracotta)"/>
      <ellipse class="ring-hole" cx="138" cy="672" rx="20" ry="18" fill="var(--sand)"/>
      <path class="blob-teal" fill="var(--teal-deep)" d="M505 443 C560 440 600 490 640 520 C700 560 730 600 722 640 C712 690 640 690 600 680 C555 670 520 720 480 745 C440 770 380 765 368 700 C355 630 370 540 415 490 C440 462 470 445 505 443 Z"/>

      <!-- front cover shapes -->
      <path class="blob-sand" fill="var(--sand)" d="M720 110 C790 95 820 150 880 150 C950 150 1060 95 1120 120 C1150 140 1140 230 1110 270 C1070 320 980 360 900 395 C840 410 760 370 700 300 C660 250 655 160 720 110 Z"/>
      <ellipse class="halo-mist" cx="846" cy="584" rx="79" ry="67" fill="var(--teal-mist)"/>
      <path class="blob-teal" fill="var(--teal-soft)" d="M950 700 C1000 690 1030 760 1070 775 C1110 790 1140 775 1149 778 V905 H900 C870 880 875 840 890 800 C905 760 910 710 950 700 Z"/>
      <path class="blob-sand" fill="var(--sand)" d="M840 662 C900 650 955 690 958 760 C960 830 920 872 860 870 C800 868 750 840 750 790 C750 740 780 675 840 662 Z"/>
      <path class="blob-tan" fill="var(--tan)" opacity="0.75" d="M680 694 C720 688 750 710 748 740 C745 770 715 785 680 782 C645 780 625 760 628 735 C632 710 650 698 680 694 Z"/>
      <path class="blob-sand" fill="var(--sand)" d="M630 820 C650 805 665 830 662 860 C658 890 640 895 620 890 C610 870 612 835 630 820 Z"/>

      <!-- illustration areas: soft tonal glows -->
      <ellipse role="img" aria-label="Boho rainbow arc in teal and tan" cx="190" cy="262" rx="70" ry="62" fill="url(#glow-teal)"/>
      <ellipse role="img" aria-label="Large teal palm frond" cx="180" cy="490" rx="130" ry="160" fill="url(#glow-teal)" opacity="0.6"/>
      <ellipse role="img" aria-label="Terracotta leafy branch" cx="420" cy="140" rx="95" ry="55" fill="url(#glow-rust)"/>
      <ellipse role="img" aria-label="Tan leafy sprig" cx="125" cy="835" rx="80" ry="65" fill="url(#glow-tan)"/>
      <ellipse role="img" aria-label="Brown looping flower line drawing" cx="355" cy="540" rx="65" ry="130" fill="url(#glow-rust)" opacity="0.6"/>
      <ellipse role="img" aria-label="Boho rainbow arc across the spine" cx="690" cy="515" rx="70" ry="58" fill="url(#glow-teal)"/>
      <ellipse role="img" aria-label="Terracotta leafy branch" cx="640" cy="760" rx="70" ry="140" fill="url(#glow-rust)" opacity="0.7"/>
      <ellipse role="img" aria-label="Hand-drawn spiral sun" cx="872" cy="205" rx="92" ry="92" fill="url(#glow-tan)"/>
      <ellipse role="img" aria-label="Teal cloud shape" cx="1085" cy="150" rx="75" ry="40" fill="url(#glow-teal)"/>
      <ellipse role="img" aria-label="Teal palm frond" cx="1080" cy="320" rx="75" ry="120" fill="url(#glow-teal)" opacity="0.6"/>
      <ellipse role="img" aria-label="Line drawing of a seated woman" cx="860" cy="730" rx="180" ry="170" fill="url(#glow-rust)" opacity="0.5"/>
      <ellipse role="img" aria-label="Brown looping flower with tan dots" cx="1045" cy="610" rx="80" ry="115" fill="url(#glow-tan)"/>
    </g>

    <!-- spine fold guides -->
    <line class="fold-guide" x1="588" y1="94" x2="588" y2="905" stroke="var(--guide)" stroke-width="0.8" stroke-dasharray="4 3"/>
    <line class="fold-guide" x1="612" y1="94" x2="612" y2="905" stroke="var(--guide)" stroke-width="0.8" stroke-dasharray="4 3"/>
  </svg>

  <h1 class="front-title"><span>I’m Unfinished,</span><span>Who Cares?</span></h1>
  <p class="spine-title">I’m Unfinished, Who Cares?</p>
  <p class="spine-author">Tobias Wexley</p>
  <div class="pen-name"><span class="pen-name-dot"></span>TOBIAS WEXLEY</div>
</main>
</body>
</html>
```